Web Button design and production

I need remote control like buttons (or your own design of buttons if I like it)
3x4 text buttons (normal, pressed, disabled)
3x1 empty button (normal, pressed, disabled)
3x6 buttons with glyph (normal, pressed, disabled)
3x288 with 24h time "00:00", "00:05", "00:10" (normal, pressed, disabled)
4 LED (red, green, orange, black)
I will upload the background image as soon as possible (black plastic)
See attached images
Q: Do the buttons have to be gray/black?
A: It should look like a high end remote control. It could be brushed aluminum as well, or something you come up with. But I guess black or dark grey would be best. The background will be picsharbor 40561739, but it's not available yet.
Q: Do I have to provide all buttons for the contest?
A: No! I only need one button (3 states) and a LED to decide. Only the winner will do the whole job.
Q: Is the Designer who wins the contest expected to complete all the extra buttons?
A: Yes, please.
Plastic

```html
<!DOCTYPE html>
<html lang="en">
<head>
<meta charset="utf-8">
<title>Remote Control Buttons – Normal, Pressed, Disabled</title>
<link href="https://fonts.googleapis.com/css2?family=Lobster&family=Arimo&display=swap" rel="stylesheet">
<style>
  :root {
    --bg-center: #333333;
    --bg-edge: #1f1f1f;
    --label: #ffffff;
    --btn-normal-top: #343434;
    --btn-normal-bottom: #2a2a2a;
    --btn-pressed: #1c1c1c;
    --btn-disabled: #2b2b2b;
    --btn-border: #171717;
    --text-normal: #e6e6e6;
    --text-disabled: #1c1c1c;
    --glyph-normal: #e0e0e0;
    --glyph-disabled: #181818;
  }
  * { box-sizing: border-box; margin: 0; padding: 0; }
  html, body { width: 1200px; height: 1200px; overflow: hidden; }
  body {
    background: radial-gradient(ellipse at 50% 45%, var(--bg-center) 0%, #2b2b2b 45%, var(--bg-edge) 100%);
    position: relative;
    font-family: "Arimo", Arial, sans-serif;
  }
  .led-row { position: absolute; top: 182px; left: 0; width: 1200px; height: 96px; }
  .led { position: absolute; top: 0; width: 96px; height: 96px; }
  .state-label {
    position: absolute; top: 364px; width: 192px; text-align: center;
    font-family: "Lobster", cursive; font-size: 34px; color: var(--label);
    text-shadow: 0 2px 3px rgba(0,0,0,0.6);
  }
  .button {
    position: absolute; width: 192px; height: 120px; border-radius: 8px;
    border: 2px solid var(--btn-border);
    display: flex; align-items: center; justify-content: center;
    font-size: 36px;
  }
  .button--normal {
    background: linear-gradient(var(--btn-normal-top), var(--btn-normal-bottom));
    box-shadow: inset 0 2px 0 rgba(255,255,255,0.08), 0 3px 4px rgba(0,0,0,0.45);
    color: var(--text-normal);
    text-shadow: 0 -2px 0 rgba(0,0,0,0.6);
  }
  .button--pressed {
    background: var(--btn-pressed);
    box-shadow: inset 0 4px 10px rgba(0,0,0,0.7), 0 2px 0 rgba(255,255,255,0.06);
    color: var(--text-normal);
  }
  .button--disabled {
    background: var(--btn-disabled);
    box-shadow: inset 0 2px 0 rgba(255,255,255,0.04), 0 2px 3px rgba(0,0,0,0.35);
    color: var(--text-disabled);
    text-shadow: 0 2px 0 rgba(255,255,255,0.06);
  }
  .col-1 { left: 264px; }
  .col-2 { left: 504px; }
  .col-3 { left: 744px; }
  .row-glyph { top: 454px; }
  .row-time { top: 670px; }
  .row-text { top: 886px; }
  .glyph { width: 60px; height: 36px; }
</style>
</head>
<body>
  <svg width="0" height="0" style="position:absolute">
    <defs>
      <radialGradient id="led-red" cx="50%" cy="40%" r="60%">
        <stop offset="0" stop-color="#ff5a5a"/><stop offset="0.6" stop-color="#e0101a"/><stop offset="1" stop-color="#8a0008"/>
      </radialGradient>
      <radialGradient id="led-green" cx="50%" cy="40%" r="60%">
        <stop offset="0" stop-color="#8dff6a"/><stop offset="0.6" stop-color="#2fc51a"/><stop offset="1" stop-color="#137a0a"/>
      </radialGradient>
      <radialGradient id="led-orange" cx="50%" cy="40%" r="60%">
        <stop offset="0" stop-color="#ffd95a"/><stop offset="0.6" stop-color="#ffa200"/><stop offset="1" stop-color="#c06400"/>
      </radialGradient>
      <radialGradient id="led-black" cx="50%" cy="40%" r="60%">
        <stop offset="0" stop-color="#777"/><stop offset="0.6" stop-color="#2a2a2a"/><stop offset="1" stop-color="#0a0a0a"/>
      </radialGradient>
      <linearGradient id="led-rim" x1="0" y1="0" x2="0" y2="1">
        <stop offset="0" stop-color="#f2f2f2"/><stop offset="1" stop-color="#9a9a9a"/>
      </linearGradient>
    </defs>
  </svg>

  <div class="led-row">
    <svg class="led" style="left:370px" viewBox="0 0 96 96" aria-label="Red LED">
      <circle cx="48" cy="48" r="46" fill="url(#led-rim)"/>
      <circle cx="48" cy="48" r="38" fill="url(#led-red)"/>
      <ellipse cx="48" cy="30" rx="22" ry="12" fill="#fff" opacity="0.45"/>
    </svg>
    <svg class="led" style="left:492px" viewBox="0 0 96 96" aria-label="Green LED">
      <circle cx="48" cy="48" r="46" fill="url(#led-rim)"/>
      <circle cx="48" cy="48" r="38" fill="url(#led-green)"/>
      <ellipse cx="48" cy="30" rx="22" ry="12" fill="#fff" opacity="0.45"/>
    </svg>
    <svg class="led" style="left:612px" viewBox="0 0 96 96" aria-label="Orange LED">
      <circle cx="48" cy="48" r="46" fill="url(#led-rim)"/>
      <circle cx="48" cy="48" r="38" fill="url(#led-orange)"/>
      <ellipse cx="48" cy="30" rx="22" ry="12" fill="#fff" opacity="0.45"/>
    </svg>
    <svg class="led" style="left:732px" viewBox="0 0 96 96" aria-label="Black LED">
      <circle cx="48" cy="48" r="46" fill="url(#led-rim)"/>
      <circle cx="48" cy="48" r="38" fill="url(#led-black)"/>
      <ellipse cx="48" cy="30" rx="22" ry="12" fill="#fff" opacity="0.35"/>
    </svg>
  </div>

  <div class="state-label col-1">Normal</div>
  <div class="state-label col-2">Pressed</div>
  <div class="state-label col-3">Disabled</div>

  <div class="button button--normal col-1 row-glyph">
    <svg class="glyph" viewBox="0 0 60 36" aria-label="Fast forward"><path d="M4 2 L28 18 L4 34 Z M30 2 L54 18 L30 34 Z" fill="var(--glyph-normal)"/></svg>
  </div>
  <div class="button button--pressed col-2 row-glyph">
    <svg class="glyph" viewBox="0 0 60 36" aria-label="Fast forward"><path d="M4 2 L28 18 L4 34 Z M30 2 L54 18 L30 34 Z" fill="var(--glyph-normal)"/></svg>
  </div>
  <div class="button button--disabled col-3 row-glyph">
    <svg class="glyph" viewBox="0 0 60 36" aria-label="Fast forward"><path d="M4 2 L28 18 L4 34 Z M30 2 L54 18 L30 34 Z" fill="var(--glyph-disabled)"/></svg>
  </div>

  <div class="button button--normal col-1 row-time">18.50</div>
  <div class="button button--pressed col-2 row-time">18.50</div>
  <div class="button button--disabled col-3 row-time">18.50</div>

  <div class="button button--normal col-1 row-text">Login</div>
  <div class="button button--pressed col-2 row-text">Login</div>
  <div class="button button--disabled col-3 row-text">Login</div>
</body>
</html>
```